Album Jacket for young indie musicians in AFRICA #2 Baraka, Tumaini And Neema (Peace, Love And Unity)

We are ZEBO SOUND (zebo-sound.example), a music label for young African musicians living in a slum. I would like to ask you to design our new album's cover jacket. The title is Baraka, Tumaini And Neema (it means "Peace, Love And Unity" in Swahili. I entrust you whether you use English words in the design or not.), musician name is Daniel Okwaro. Add our label logo (we have various versions and can provide). I attached Daniel Okwaro's photo also. Please listen to the music of the album on Soundcloud. https://audiovault.example/tags/danielokwaro

Target Market(s)

International. not only African music funs.

Requirements
Must have
• Title, Musician's name, ZEBO SOUND Logo
• In order to upload to iTunes, I require the final that the following conditions are met.
• 1400 x 1400 pixels
• JPG file type
• 72 - 300dpi (300dpi is the best)
• Less than 25mb
• RGB color scheme (not CMYK)
Nice to have
• His music is something bright and little funny. Please express the tone of music in the design.
Should not have
• African traditional image

```html
<!DOCTYPE html>
<html lang="en">
<head>
<meta charset="utf-8">
<title>Baraka, Tumaini And Neema — Daniel Okwaro</title>
<link rel="stylesheet" href="https://fonts.googleapis.com/css2?family=Fredoka:wght@700&family=Lobster&display=swap">
<style>
  :root {
    --stage: #4b4d4d;
    --cover-yellow: #fdc51f;
    --title-yellow: #fdc51f;
    --ink: #1f1f1f;
    --halo: #ffffff;
    --warm-red: #e8452a;
    --warm-orange: #f6a02a;
    --cool-blue: #2a6cc4;
    --cool-light: #7cc4ec;
  }
  * { margin: 0; padding: 0; box-sizing: border-box; }
  html, body {
    width: 1200px;
    height: 815px;
    overflow: hidden;
    background: var(--stage);
  }
  .album-cover {
    position: absolute;
    left: 260px;
    top: 67px;
    width: 680px;
    height: 680px;
    background: var(--cover-yellow);
    overflow: hidden;
  }
  .artwork-area {
    position: absolute;
    left: 30px;
    top: 30px;
    width: 620px;
    height: 620px;
    border: 12px solid var(--halo);
    background: linear-gradient(135deg, var(--warm-red) 0%, var(--warm-orange) 40%, var(--cool-blue) 62%, var(--cool-light) 100%);
  }
  .artist-name {
    position: absolute;
    top: 38px;
    right: 30px;
    font-family: "Lobster", cursive;
    font-size: 46px;
    line-height: 1.2;
    color: var(--halo);
    text-shadow:
      3px 0 0 var(--ink), -3px 0 0 var(--ink), 0 3px 0 var(--ink), 0 -3px 0 var(--ink),
      2px 2px 0 var(--ink), -2px -2px 0 var(--ink), 2px -2px 0 var(--ink), -2px 2px 0 var(--ink);
  }
  .album-title {
    position: absolute;
    top: 138px;
    left: 20px;
    right: 0;
    text-align: center;
    font-family: "Fredoka", sans-serif;
    font-weight: 700;
    font-size: 96px;
    line-height: 1.04;
    text-transform: uppercase;
    color: var(--title-yellow);
    letter-spacing: 1px;
    text-shadow:
      5px 0 0 var(--ink), -5px 0 0 var(--ink), 0 5px 0 var(--ink), 0 -5px 0 var(--ink),
      4px 4px 0 var(--ink), -4px -4px 0 var(--ink), 4px -4px 0 var(--ink), -4px 4px 0 var(--ink),
      5px 2px 0 var(--ink), -5px 2px 0 var(--ink), 5px -2px 0 var(--ink), -5px -2px 0 var(--ink),
      2px 5px 0 var(--ink), -2px 5px 0 var(--ink), 2px -5px 0 var(--ink), -2px -5px 0 var(--ink);
  }
  .album-title span { display: block; }
  .label-mark {
    position: absolute;
    left: 30px;
    bottom: 24px;
    display: flex;
    align-items: center;
    gap: 8px;
  }
  .label-square {
    width: 40px;
    height: 40px;
    background: var(--ink);
  }
  .label-name {
    font-family: "Fredoka", sans-serif;
    font-weight: 700;
    font-size: 16px;
    color: var(--ink);
    letter-spacing: 0.5px;
  }
</style>
</head>
<body>
  <section class="album-cover">
    <div class="artwork-area" role="img" aria-label="Illustration area: a heart formed by a red and orange flame and a blue ocean wave"></div>
    <p class="artist-name">Daniel Okwaro</p>
    <h1 class="album-title">
      <span>Baraka</span>
      <span>Tumaini</span>
      <span>And</span>
      <span>Neema</span>
    </h1>
    <div class="label-mark">
      <span class="label-square"></span>
      <span class="label-name">ZEBO SOUND</span>
    </div>
  </section>
</body>
</html>
```